Corvanta Business cards template

We're looking for something modern and elegant. We are a reseller of technology (computers, datacenter, etc). Color theme would be "only" white with the incorporation of the blue that's present on our website (Corvanta.com) and logo file. We would like for the card to provide all the necessary info for the specific person (Phone#, fax#, email, name, website URL) . I'm attaching the logo file to this request. Please have it show Montreal/New York somewhere, without providing specific addresses.

Target Market(s)

All b2b

Industry/Entity Type

Business

Contact Information for Business Card

Please have the color scheme be represented by only the white and blue from our website (Corvanta.com) and logo. We would like to logo on the card, but not big and overwhelming. This card will be used as a template for anybody within the company, it should display the user's name, phone#, fax#, email, job title and website URL. Please have it show Montreal/New York somewhere, without providing our specific addresses. Really, we're looking for a clean, simple and elegant look.

Font styles to use
Serif

Requirements
Must have
• Please see card details
Nice to have
• Please see card details
Should not have
• Anything tacky or tagline.

```html
<!DOCTYPE html>
<html lang="en">
<head>
<meta charset="UTF-8">
<title>Corvanta Business Card</title>
<link href="https://fonts.googleapis.com/css2?family=Montserrat:wght@400;500;700&display=swap" rel="stylesheet">
<style>
  :root {
    --brand-blue: #0b84d4;
    --brand-blue-deep: #0a6fc0;
    --card-white: #ffffff;
    --ink: #3a3a3a;
    --backdrop: #2d2d2d;
  }
  * { box-sizing: border-box; margin: 0; padding: 0; }
  html, body { width: 1200px; height: 900px; overflow: hidden; }
  body {
    background: var(--backdrop);
    font-family: "Montserrat", Arial, sans-serif;
    display: flex;
    flex-direction: column;
    align-items: center;
    justify-content: center;
    gap: 56px;
  }
  .card {
    position: relative;
    width: 640px;
    height: 366px;
    overflow: hidden;
  }
  .card-front {
    background: linear-gradient(135deg, var(--brand-blue-deep) 0%, var(--brand-blue) 100%);
    display: flex;
    align-items: center;
    justify-content: center;
  }
  .wordmark {
    font-family: "Montserrat", Arial, sans-serif;
    font-weight: 500;
    letter-spacing: 1px;
  }
  .card-front .wordmark {
    color: var(--card-white);
    font-size: 62px;
  }
  .card-back { background: var(--card-white); }
  .band {
    position: absolute;
    height: 20px;
    background: var(--brand-blue);
  }
  .band-top { top: 0; left: 0; width: 270px; }
  .band-bottom { bottom: 0; right: 0; width: 290px; }
  .card-back .wordmark {
    position: absolute;
    left: 58px;
    top: 158px;
    color: var(--brand-blue);
    font-size: 34px;
  }
  .contact {
    position: absolute;
    left: 360px;
    top: 78px;
    color: var(--ink);
  }
  .contact-name {
    color: var(--brand-blue);
    font-weight: 700;
    font-size: 22px;
    letter-spacing: 0.5px;
  }
  .contact-title {
    font-size: 17px;
    font-weight: 500;
    margin-top: 4px;
    margin-bottom: 18px;
    letter-spacing: 0.5px;
  }
  .contact-list { list-style: none; }
  .contact-list li {
    display: flex;
    align-items: center;
    gap: 10px;
    font-size: 14px;
    line-height: 26px;
    white-space: nowrap;
  }
  .contact-list .gap-before { margin-top: 10px; }
  .icon { width: 15px; height: 15px; fill: var(--brand-blue); flex: none; }
  .icon-line { fill: none; stroke: var(--brand-blue); stroke-width: 1.4; }
</style>
</head>
<body>

<section class="card card-front" aria-label="Card front">
  <span class="wordmark">Corvanta</span>
</section>

<section class="card card-back" aria-label="Card back">
  <div class="band band-top"></div>
  <div class="band band-bottom"></div>
  <span class="wordmark">Corvanta</span>

  <div class="contact">
    <p class="contact-name">JOHN DOE</p>
    <p class="contact-title">OWNER</p>
    <ul class="contact-list">
      <li>
        <svg class="icon" viewBox="0 0 16 16" aria-hidden="true"><path d="M3.6 1.2 5.8 1l1.2 3.4-1.5 1.2a9 9 0 0 0 4.9 4.9l1.2-1.5 3.4 1.2-.2 2.2c-.1.9-.9 1.5-1.8 1.4C6.7 13.1 2.9 9.3 2.2 3c-.1-.9.5-1.7 1.4-1.8z"/></svg>
        014 555 0192
      </li>
      <li>
        <svg class="icon" viewBox="0 0 16 16" aria-hidden="true"><path d="M4 1h7l2 2v3H4zM2 7h12a1 1 0 0 1 1 1v5H1V8a1 1 0 0 1 1-1zm3 4v4h6v-4z"/></svg>
        014 555 0193
      </li>
      <li class="gap-before">
        <svg class="icon" viewBox="0 0 16 16" aria-hidden="true"><path d="M1 3h14v1.2L8 9 1 4.2zm0 2.6 7 4.8 7-4.8V13H1z"/></svg>
        JohnDoe@corvanta.com
      </li>
      <li>
        <svg class="icon icon-line" viewBox="0 0 16 16" aria-hidden="true"><circle cx="8" cy="8" r="6.3"/><ellipse cx="8" cy="8" rx="2.8" ry="6.3"/><path d="M1.7 8h12.6"/></svg>
        www.corvanta.com
      </li>
      <li>
        <svg class="icon" viewBox="0 0 16 16" aria-hidden="true"><path d="M8 1a5 5 0 0 0-5 5c0 3.6 5 9 5 9s5-5.4 5-9a5 5 0 0 0-5-5zm0 7a2 2 0 1 1 0-4 2 2 0 0 1 0 4z"/></svg>
        Lakeport | Westbridge
      </li>
    </ul>
  </div>
</section>

</body>
</html>
```